FSA Expiring Soon 2023

Hi,
Looking to upgrade the design of current flyer to be used as an e-blast.
-8.5"x11"
-Under 5MB
-Several formats, PDF, .ai, jpeg, png

This flyer should be simple, yet eye catching. The goal is to remind patients that their Flexible Spending Account (FSA) will be expiring soon and that they can use their FSA or HSA to purchase most of our over the counter items, including inserts and shoes.

-must include: Some insurance plans require a letter of medical necessity
-must include: Each flexible spending account varies on their expiration date
- stock images must be free

I'll attach our logo and old flyer as well for reference.

Thank you,
Oscar

```html
<!DOCTYPE html>
<html lang="en">
<head>
<meta charset="utf-8">
<title>Use Your FSA Funds – Hillcrest Foot &amp; Ankle</title>
<link href="https://fonts.googleapis.com/css2?family=Roboto:wght@400;700;900&display=swap" rel="stylesheet">
<style>
  :root {
    --black: #000000;
    --teal: #66c7b0;
    --orange: #f37f4a;
    --red: #e60000;
    --red-dark: #a30000;
    --white: #ffffff;
    --ink: #0d0d0d;
    --grey: #555555;
    --photo-warm: #d9a586;
    --photo-cool: #9aa3b4;
  }
  * { margin: 0; padding: 0; box-sizing: border-box; }
  html, body { width: 927px; height: 1200px; overflow: hidden; background: var(--white); }
  body { font-family: "Roboto", Arial, sans-serif; }
  .flyer { position: relative; width: 927px; height: 1200px; overflow: hidden; background: var(--white); }

  .header { position: absolute; left: 0; top: 0; width: 927px; height: 119px; background: var(--black); }
  .brand { position: absolute; left: 125px; top: 12px; color: var(--orange); font-weight: 900; text-align: right; width: 308px; }
  .brand-name { font-size: 36px; line-height: 40px; letter-spacing: 0.5px; }
  .brand-site { font-size: 17px; line-height: 22px; margin-top: 2px; }
  .call-label { position: absolute; left: 709px; top: 31px; color: var(--white); font-weight: 700; font-size: 16px; }
  .call-icon { position: absolute; left: 805px; top: 23px; width: 37px; height: 37px; }
  .phone { position: absolute; right: 85px; top: 62px; color: var(--white); font-weight: 900; font-size: 36px; letter-spacing: 1px; }

  .photo { position: absolute; left: 0; top: 119px; width: 927px; height: 552px;
    background: linear-gradient(120deg, var(--photo-cool) 0%, #e9dcd3 30%, var(--photo-warm) 55%, #e8b9a0 75%, #3a3a3a 100%); }

  .web-band { position: absolute; left: 0; top: 615px; width: 448px; height: 64px; background: var(--orange); }
  .web-band svg { position: absolute; left: 76px; top: 18px; }
  .web-band span { position: absolute; left: 117px; top: 14px; color: var(--white); font-weight: 700; font-size: 27px; }

  .fsa-panel { position: absolute; left: 448px; top: 486px; width: 394px; height: 646px; background: var(--teal); }
  .fsa-panel::before { content: ""; position: absolute; left: 0; top: 0; width: 100%; height: 193px; background: rgba(80,170,150,0.35); }
  .fsa-panel h2 { position: absolute; left: 40px; top: 70px; font-weight: 900; font-size: 49px; line-height: 62.3px; letter-spacing: 0.3px; }
  .fsa-panel .light { color: var(--white); display: block; }
  .fsa-panel .dark { color: var(--ink); display: block; }

  .ribbon { position: absolute; left: 449px; top: 454px; width: 388px; height: 86px; }
  .ribbon span { position: absolute; left: 0; top: 20px; width: 100%; text-align: center; color: var(--white); font-weight: 900; font-size: 42px; letter-spacing: 3px; }

  .lead { position: absolute; left: 75px; top: 700px; width: 360px; font-weight: 900; font-size: 20.5px; line-height: 30.6px; letter-spacing: 0.3px; color: var(--ink); }
  .notes { position: absolute; left: 75px; top: 837px; width: 380px; list-style: none; }
  .notes li { position: relative; padding-left: 19px; color: var(--grey); font-size: 16px; line-height: 24px; margin-bottom: 24px; }
  .notes li::before { content: "»"; position: absolute; left: 0; top: 0; color: var(--orange); font-weight: 700; }

  .office { position: absolute; width: 200px; }
  .office h3 { color: var(--orange); font-weight: 700; font-size: 13px; text-decoration: underline; margin-bottom: 9px; }
  .office p { color: var(--grey); font-size: 11px; line-height: 19.3px; }
  .office-brookfield { left: 75px; top: 988px; }
  .office-maple-grove { left: 257px; top: 988px; }
  .office-cedar-hollow { left: 75px; top: 1091px; }

  .code { position: absolute; right: 15px; top: 1166px; font-weight: 700; font-size: 10px; color: var(--ink); }
  .footer-line { position: absolute; left: 0; bottom: 0; width: 927px; height: 4px; background: var(--teal); }
</style>
</head>
<body>
<div class="flyer">
  <header class="header">
    <div class="brand">
      <div class="brand-name">HILLCREST<br>FOOT &amp; ANKLE</div>
      <div class="brand-site">STRIDEWELLFEET.COM</div>
    </div>
    <div class="call-label">Call Us On:</div>
    <svg class="call-icon" viewBox="0 0 37 37" aria-hidden="true">
      <circle cx="18.5" cy="18.5" r="18.5" fill="var(--teal)"/>
      <path d="M13 11c1-.6 2-.3 2.5.6l1.3 2.6c.4.8.2 1.6-.5 2.1l-1 .8c.8 2 2.4 3.6 4.4 4.4l.8-1c.5-.7 1.3-.9 2.1-.5l2.6 1.3c.9.5 1.2 1.5.6 2.5l-.8 1.2c-.7 1-2 1.4-3.2 1-4.5-1.5-8-5-9.5-9.5-.4-1.2 0-2.5 1-3.2z" fill="var(--white)"/>
    </svg>
    <div class="phone">877-555-0142</div>
  </header>

  <div class="photo" role="img" aria-label="Photo of a person in athletic wear fastening a grey ankle weight over a blue running shoe in a bright gym"></div>

  <div class="web-band">
    <svg width="28" height="28" viewBox="0 0 28 28" aria-hidden="true" fill="none" stroke="var(--white)" stroke-width="1.8">
      <circle cx="14" cy="14" r="12.5"/>
      <ellipse cx="14" cy="14" rx="5.5" ry="12.5"/>
      <line x1="1.5" y1="14" x2="26.5" y2="14"/>
      <line x1="3.5" y1="7.5" x2="24.5" y2="7.5"/>
      <line x1="3.5" y1="20.5" x2="24.5" y2="20.5"/>
      <line x1="14" y1="1.5" x2="14" y2="26.5"/>
    </svg>
    <span>StrideWellFeet.com</span>
  </div>

  <section class="fsa-panel">
    <h2>
      <span class="light">USE YOUR</span>
      <span class="light">FLEXIBLE</span>
      <span class="light">SPENDING</span>
      <span class="light">ACCOUNT</span>
      <span class="light">FUNDS</span>
      <span class="light">BEFORE THEY</span>
      <span class="dark">EXPIRE AT</span>
      <span class="dark">THE END OF</span>
      <span class="dark">THE YEAR!</span>
    </h2>
  </section>

  <div class="ribbon">
    <svg width="388" height="86" viewBox="0 0 388 86" aria-hidden="true">
      <polygon points="0,32 14,0 374,0 388,32" fill="var(--red-dark)"/>
      <polygon points="10,0 378,0 362,86 26,86" fill="var(--red)"/>
    </svg>
    <span>ENDS SOON</span>
  </div>

  <p class="lead">MOST OF OUR OVER THE<br>COUNTER PRODUCTS ARE<br>FSA/HSA ELIGIBLE, INCLUDING<br>ORTHOTICS AND SHOES.</p>

  <ul class="notes">
    <li>Some insurance plans require a letter of medical<br>necessity</li>
    <li>Each flexible spending account varies on their<br>expiration date</li>
  </ul>

  <div class="office office-brookfield">
    <h3>BROOKFIELD OFFICE</h3>
    <p>58 Orchard Ridge Dr.<br>Ste 120<br>Brookfield, ST 10481</p>
  </div>
  <div class="office office-maple-grove">
    <h3>MAPLE GROVE OFFICE</h3>
    <p>2210 Meadowlark Blvd.<br>Ste 305<br>Maple Grove, ST 10492</p>
  </div>
  <div class="office office-cedar-hollow">
    <h3>CEDAR HOLLOW OFFICE</h3>
    <p>417 Wellness Way<br>Cedar Hollow, ST 10517</p>
  </div>

  <div class="code">C58</div>
  <div class="footer-line"></div>
</div>
</body>
</html>
```